Business Card Design

I need a business card, for my company that reflects fire and building.
I am a bushfire consultant, and my role is to determine a fire assessment for new houses being built, in bushfire prone areas.
Compiling a report on what building materials will need to be used, and whether or not parts of the block will need to be cleared of vegetation. I would like to see the colours of fire, and possibly a house on there as well, or maybe just fire. This will probably be used as a logo as well, and will reflect the severity of fire to housing.
Target Market(s)
New home builders residential
Industry/Entity Type
Building
Contact Information for Business Card
Emberline Advisory Coastal Range
Bushfire Consultant
Garth Pemberly
0438 261 904

```html
<!DOCTYPE html>
<html lang="en">
<head>
<meta charset="utf-8">
<title>Emberline Advisory – Business Card</title>
<link rel="stylesheet" href="https://fonts.googleapis.com/css2?family=Days+One&family=Cinzel:wght@600&family=Arimo:wght@400&display=swap">
<style>
  :root {
    --stage: #c9c9c9;
    --paper: #ffffff;
    --ink: #111111;
    --night: #0b0b0b;
    --night-soft: #1e1e1e;
    --ember: #f26a1b;
    --ember-deep: #d9420f;
    --flame-gold: #ffb52e;
    --flame-red: #c8260a;
    --silver: #9a9a9a;
    --name-orange: #f5a623;
  }
  * { box-sizing: border-box; margin: 0; padding: 0; }
  html, body { width: 1200px; height: 900px; overflow: hidden; }
  body {
    background: var(--stage);
    position: relative;
    font-family: "Arimo", Arial, sans-serif;
  }
  .card {
    position: absolute;
    top: 297px;
    width: 500px;
    height: 306px;
    border-radius: 24px;
    overflow: hidden;
  }
  .card-front { left: 70px; background: var(--paper); }
  .card-back { left: 630px; background: var(--night); }

  /* front */
  .brand {
    position: absolute;
    top: 0; left: 0; right: 0;
    height: 172px;
    display: flex;
    align-items: center;
    justify-content: center;
    gap: 14px;
  }
  .brand-mark {
    width: 30px; height: 30px;
    background: var(--ember);
  }
  .brand-name {
    font-family: "Days One", sans-serif;
    font-size: 30px;
    color: var(--ink);
  }
  .tagline-band {
    position: absolute;
    top: 172px; left: 0; right: 0;
    height: 22px;
    background: linear-gradient(to bottom, var(--ember) 0 3px, var(--ember-deep) 3px 19px, var(--ember) 19px);
    display: flex;
    align-items: center;
    justify-content: center;
  }
  .tagline {
    font-family: "Cinzel", serif;
    font-weight: 600;
    font-size: 13px;
    letter-spacing: 2.6px;
    color: var(--ink);
  }
  .contact-panel {
    position: absolute;
    top: 194px; left: 0; right: 0; bottom: 0;
    background: radial-gradient(ellipse at 50% 30%, var(--night-soft), var(--night) 75%);
    padding-top: 18px;
    text-align: center;
  }
  .contact-name {
    color: var(--name-orange);
    font-size: 23px;
    line-height: 30px;
  }
  .contact-phone {
    color: var(--paper);
    font-size: 25px;
    line-height: 32px;
  }

  /* back */
  .flame-field {
    position: absolute;
    left: 0; right: 0; bottom: 0;
    height: 250px;
    background: linear-gradient(to top, var(--flame-red) 0%, var(--ember) 40%, var(--flame-gold) 70%, rgba(11,11,11,0) 100%);
  }
  .back-brand {
    position: absolute;
    left: 0; right: 0;
    top: 200px;
    display: flex;
    justify-content: center;
    align-items: center;
    gap: 14px;
  }
  .back-brand .brand-mark { background: var(--silver); width: 34px; height: 34px; }
  .back-brand .brand-name { color: var(--silver); font-size: 36px; }
</style>
</head>
<body>
  <section class="card card-front">
    <div class="brand">
      <span class="brand-mark"></span>
      <span class="brand-name">Emberline Advisory</span>
    </div>
    <div class="tagline-band">
      <p class="tagline">COASTAL RANGE BUSHFIRE CONSULTANT</p>
    </div>
    <div class="contact-panel">
      <p class="contact-name">Garth Pemberly</p>
      <p class="contact-phone">0438 261 904</p>
    </div>
  </section>

  <section class="card card-back">
    <div class="flame-field" role="img" aria-label="Illustration of tall orange and yellow flames rising across the card"></div>
    <div class="back-brand">
      <span class="brand-mark"></span>
      <span class="brand-name">Emberline Advisory</span>
    </div>
  </section>
</body>
</html>
```